PPT Design Project for an educational startup

We seek a PPT design for a new company based in Japan called "Brivorent".
We provide PPT slide-based educational videos for free.
Please see the link below. You will see some videos.
http://velmora-example.jp/
The current template is also attached.
As we are changing our service name from Velmora to Brivorent, we are considering to change the PPT template as well.
Here are some notes regarding this project.
1. We need three pages;
- Title page: Letters for the tile and the logo are necessary. Some pictorial marks or other design would be appreciated.
- Contents page: Just one line to divide the message part and contents part should be sufficient. Please do not spend your time here.
- Final page: The word "Thank you for watching!" in the center. Some pictorial marks or other design would be appreciated.
2. Please use light green, orange, and purple as main colors. (Same as the current template)
3. You don't have to think about the font-style. This is going to be Japanese font, so we will take care of this.
4. Background color needs to be white, as the slides could be printed out.
5. We use Powerpoint for Mac.
6. No copyright section required, as these slides will be creative commons. Instead of the copyright section, please put the creative commons mark in all slides. (which is in the original template attached)
Updates
Please forget about the creative commons mark.
Hi all,
Target Market(s)
16-25 years old people, who are highly educated or highly motivated for education
Industry/Entity Type
It Company
Requirements
Must have
- 1. Creative commons mark (which is in the original template)
Should not have
- 1. Copyright mark

```html
<!DOCTYPE html>
<html lang="en">
<head>
<meta charset="utf-8">
<title>Brivorent – Title Slide</title>
<link rel="stylesheet" href="https://fonts.googleapis.com/css2?family=Open+Sans:wght@400;600;700&display=swap">
<style>
  :root {
    --brand-green: #7dc242;
    --brand-orange: #f5a436;
    --brand-grey: #7a7a7a;
    --corner-grey: #b7b7b7;
    --rule-grey: #d4d4d4;
    --ink: #111111;
    --paper: #ffffff;
  }
  * { margin: 0; padding: 0; box-sizing: border-box; }
  html, body {
    width: 1200px;
    height: 900px;
    overflow: hidden;
    background: var(--paper);
  }
  .slide {
    position: relative;
    width: 1200px;
    height: 900px;
    background: var(--paper);
    font-family: "Open Sans", "Calibri", sans-serif;
    overflow: hidden;
  }
  .brand-name {
    position: absolute;
    left: 54px;
    top: 62px;
    font-size: 72px;
    font-weight: 700;
    letter-spacing: -1px;
    color: var(--brand-grey);
    line-height: 1;
  }
  .corner-squares {
    position: absolute;
    top: 0;
    right: 0;
  }
  .title-block {
    position: absolute;
    left: 60px;
    top: 386px;
    white-space: nowrap;
    line-height: 1;
  }
  .title-lead {
    font-size: 62px;
    font-weight: 700;
    color: var(--brand-green);
  }
  .title-rest {
    font-size: 48px;
    font-weight: 400;
    color: var(--ink);
    margin-left: 10px;
  }
  .title-rule {
    position: absolute;
    left: 0;
    top: 468px;
    width: 840px;
    height: 3px;
    background: linear-gradient(to right, var(--rule-grey) 0%, var(--rule-grey) 55%, rgba(212,212,212,0) 100%);
  }
  .title-shade {
    position: absolute;
    left: 0;
    top: 471px;
    width: 840px;
    height: 120px;
    background:
      linear-gradient(to bottom, rgba(235,235,235,0.9) 0%, rgba(255,255,255,0) 100%);
    -webkit-mask-image: linear-gradient(to right, #000 0%, #000 55%, transparent 100%);
            mask-image: linear-gradient(to right, #000 0%, #000 55%, transparent 100%);
  }
  .corner-triangle {
    position: absolute;
    left: 0;
    bottom: 0;
  }
</style>
</head>
<body>
  <main class="slide">
    <div class="brand-name">Brivorent</div>

    <svg class="corner-squares" width="130" height="172" viewBox="0 0 130 172" aria-hidden="true">
      <rect x="67" y="0" width="63" height="63" fill="var(--brand-orange)"/>
      <rect x="5" y="78" width="64" height="62" fill="var(--brand-orange)"/>
      <rect x="85" y="108" width="45" height="64" fill="var(--brand-orange)"/>
    </svg>

    <h1 class="title-block">
      <span class="title-lead">Presentation</span><span class="title-rest">Title here</span>
    </h1>

    <div class="title-rule"></div>
    <div class="title-shade"></div>

    <svg class="corner-triangle" width="160" height="234" viewBox="0 0 160 234" aria-hidden="true">
      <polygon points="0,0 158,234 0,234" fill="var(--corner-grey)"/>
    </svg>
  </main>
</body>
</html>
```